Vexa Wellness Business Card

A Double Sided Business Card

I am a private company in Melbourne, Australia, working in the Health industry. I am a nutritionist and lifestyle coach, whom specialises in using raw foods ie. fruits/nuts/vegetables to help heal my clients and enable them to achieve their ultimate state of health.

I want a sophisticated design and colour for my card that appeals to both men and women from teenage through to elderly.

Front of Card:

Red apple peel spiral in the shape of an apple. I would like a leaf/leaves coming off the stem of the apple. Please see attachments for example.

***On Right Hand side of Image is business Name: Vexa Wellness

Underneath LOGO use slogan " Let Food Be Your Medicine"

***Use Deep Red and Blues for Text Colouring

Back of Card:

Marisol Tenzing
Nutritional Specialist and Lifestyle Coach

Specialising in: Diseased Conditions
Weight Management
Achieving your Ultimate State of Health

enquiries@vexawellness.example 0493 517 642

**Make sure the front design of the card flows onto the back.
Updates

Email address has been amended, Also more specific details have been given for apple peel Image, and another image attached as example of Leaf on stem of apple.

I little more insight into what sort of feel were trying to create. We're apart of the health industry, and we want the card to have a medical/clinical feeling about it.

Target Market(s)

Males and Females from teenages to elderly

Industry/Entity Type

Business

Requirements
Must have
• Red Apple Peel Spiral, in the shape of an apple, with a leaf/leaves attached to stem.
***Must be in the shape of an apple
***Please use coloring on inside of apple peel to resemble inside of an apple.
Nice to have
• I would like my card to have a clinical feel.
Should not have
• We don't want the image of the apple to look like a Christmas decoration

```html
<!DOCTYPE html>
<html lang="en">
<head>
<meta charset="utf-8">
<title>Vexa Wellness Business Card</title>
<link rel="stylesheet" href="https://fonts.googleapis.com/css2?family=Quicksand:wght@500;600;700&display=swap">
<style>
  :root {
    --backdrop: #ecebe8;
    --card: #ffffff;
    --orange: #f5a033;
    --orange-deep: #f08a24;
    --grey: #dcdcdc;
    --grey-soft: #ededed;
    --red: #d7262b;
    --navy: #252d6e;
    --blue: #3a4fa8;
    --green: #57a838;
    --white: #ffffff;
  }
  * { margin: 0; padding: 0; box-sizing: border-box; }
  html, body {
    width: 1200px; height: 900px; overflow: hidden;
    background: var(--backdrop);
    font-family: "Quicksand", sans-serif;
  }
  .canvas { position: relative; width: 1200px; height: 900px; }
  .card {
    position: absolute; width: 600px; height: 375px;
    background: var(--card);
    box-shadow: 0 10px 24px rgba(0,0,0,0.18);
    overflow: hidden;
  }
  .card-back { left: 50px; top: 60px; }
  .card-front { left: 560px; top: 470px; }
  .card-art { position: absolute; inset: 0; width: 100%; height: 100%; }

  .details { position: absolute; left: 0; right: 0; top: 128px; text-align: center; padding-left: 90px; }
  .holder-name { color: var(--red); font-size: 28px; font-weight: 600; line-height: 1.1; }
  .holder-role { color: var(--navy); font-size: 19px; font-weight: 600; line-height: 1.15; }
  .specialties { margin-top: 24px; color: var(--navy); font-size: 17px; font-weight: 600; line-height: 1.3; }
  .specialties-title { color: var(--navy); font-size: 20px; }

  .contact { position: absolute; left: 42px; top: 312px; list-style: none; }
  .contact li { display: flex; align-items: center; gap: 9px; color: var(--white); font-size: 18px; font-weight: 600; height: 30px; }
  .contact-icon { width: 22px; height: 22px; }

  .mini-name { position: absolute; right: 22px; top: 300px; color: var(--red); font-size: 13px; font-weight: 700; }

  .brand { position: absolute; left: 110px; top: 92px; display: flex; align-items: center; gap: 18px; }
  .brand-dot { width: 104px; height: 104px; border-radius: 50%; background: var(--red); flex: none; }
  .brand-name { color: var(--red); font-size: 44px; font-weight: 700; line-height: 1; }
  .slogan { color: var(--green); font-size: 20px; font-weight: 600; margin-top: 6px; }
</style>
</head>
<body>
<main class="canvas">

  <section class="card card-back" aria-label="Back of card">
    <svg class="card-art" viewBox="0 0 600 375" aria-hidden="true">
      <path fill="var(--grey-soft)" d="M330 0 C450 20 560 40 600 20 L600 0 Z"/>
      <path fill="var(--grey)" d="M380 190 C470 200 560 230 570 300 C520 260 440 230 340 225 Z"/>
      <path fill="var(--orange)" d="M0 118 C200 150 430 110 600 58 L600 140 C430 200 230 232 0 212 Z"/>
      <path fill="var(--grey)" d="M0 268 C160 250 330 250 600 276 L600 300 C380 290 180 290 0 300 Z"/>
      <path fill="var(--orange-deep)" d="M0 300 C200 294 420 290 520 300 C460 340 300 375 200 375 L0 375 Z"/>
    </svg>

    <div class="details">
      <h1 class="holder-name">Marisol Tenzing</h1>
      <p class="holder-role">Nutritional Specialist</p>
      <p class="holder-role">Lifestyle Coach</p>
      <div class="specialties">
        <p class="specialties-title">Specialising in:</p>
        <p>·Diseased Conditions &nbsp;·Weight Management</p>
        <p>·Achieving your Ultimate State of Health</p>
      </div>
    </div>

    <ul class="contact">
      <li>
        <svg class="contact-icon" viewBox="0 0 22 22" aria-hidden="true">
          <circle cx="11" cy="11" r="11" fill="var(--red)"/>
          <circle cx="11" cy="11" r="6.5" fill="none" stroke="var(--white)" stroke-width="1.4"/>
          <ellipse cx="11" cy="11" rx="3" ry="6.5" fill="none" stroke="var(--white)" stroke-width="1.2"/>
          <line x1="4.5" y1="11" x2="17.5" y2="11" stroke="var(--white)" stroke-width="1.2"/>
        </svg>
        enquiries@vexawellness.example
      </li>
      <li>
        <svg class="contact-icon" viewBox="0 0 22 22" aria-hidden="true">
          <circle cx="11" cy="11" r="11" fill="var(--red)"/>
          <path fill="var(--white)" d="M7 5.5 L9.3 5 L10.4 8.2 L9 9.3 C9.7 11 11 12.3 12.7 13 L13.8 11.6 L17 12.7 L16.5 15 C11 15.5 6.5 11 7 5.5 Z"/>
        </svg>
        0493 517 642
      </li>
    </ul>

    <p class="mini-name">Vexa Wellness</p>
  </section>

  <section class="card card-front" aria-label="Front of card">
    <svg class="card-art" viewBox="0 0 600 375" aria-hidden="true">
      <path fill="var(--grey-soft)" d="M0 0 L600 0 L600 40 C420 60 200 40 0 80 Z"/>
      <path fill="var(--grey)" d="M0 210 C150 195 330 200 420 240 L0 260 Z"/>
      <path fill="var(--orange)" d="M0 255 C200 240 420 230 600 200 L600 275 C420 320 200 340 0 340 Z"/>
      <path fill="var(--grey)" d="M40 375 C120 345 300 340 520 350 C560 355 590 365 600 375 Z"/>
    </svg>

    <div class="brand">
      <span class="brand-dot" aria-hidden="true"></span>
      <div>
        <p class="brand-name">Vexa Wellness</p>
        <p class="slogan">Let Food Be Your Medicine</p>
      </div>
    </div>
  </section>

</main>
</body>
</html>
```